Vantor Medica Innovative Business Card

Stunning business card. Background will be black. Letters in gold. Modern yet simple design that is attention grabbing. QR code leading to site. Attractive primarily to males ages 30 to 50 but also to females in same age range looking for beauty and mental health products

Target Market(s)

Males in the 30-50 age demographics

Industry/Entity Type

Pharmaceuticals selling erectile dysfunction and mens health medications

Contact Information for Business Card

www.vantormedica.example; (775) BUY-KELO; info@vantormedica.example

Colors
FFC000
F8CF3A
FAE287
FDF2CF
FEFAEE

Requirements
Must have
• Black business card with gold letters.
Nice to have
• perhaps just the logo or the "R" icon by itself on one side
Should not have
• too much content so it does not look busy

```html
<!DOCTYPE html>
<html lang="en">
<head>
<meta charset="utf-8">
<title>Vantor Medica Business Card</title>
<link href="https://fonts.googleapis.com/css2?family=Source+Sans+3:wght@400;600;700&display=swap" rel="stylesheet">
<style>
  :root {
    --backdrop: #e6e6e6;
    --card: #2b2a29;
    --gold: #d9b43a;
    --gold-text: #e4c03c;
  }
  * { box-sizing: border-box; margin: 0; padding: 0; }
  html, body {
    width: 1200px;
    height: 960px;
    overflow: hidden;
    background: var(--backdrop);
    font-family: "Source Sans 3", "Source Sans Pro", sans-serif;
  }
  .canvas {
    position: relative;
    width: 1200px;
    height: 960px;
  }
  .card {
    position: absolute;
    left: 298px;
    width: 607px;
    height: 347px;
    background: var(--card);
  }
  .card--front { top: 108px; }
  .card--back { top: 508px; }

  .front-mark {
    position: absolute;
    inset: 0;
    display: flex;
    align-items: center;
    justify-content: center;
    gap: 18px;
  }
  .front-mark__dot {
    width: 34px;
    height: 34px;
    border-radius: 50%;
    background: var(--gold);
  }
  .front-mark__name {
    font-size: 44px;
    font-weight: 700;
    color: var(--gold);
    letter-spacing: 1px;
  }

  .brand {
    position: absolute;
    left: 62px;
    top: 150px;
    width: 230px;
    display: flex;
    align-items: center;
    justify-content: center;
    gap: 10px;
  }
  .brand__dot {
    width: 20px;
    height: 20px;
    border-radius: 50%;
    background: var(--gold);
  }
  .brand__name {
    font-size: 30px;
    font-weight: 700;
    color: var(--gold);
    letter-spacing: 0.5px;
    white-space: nowrap;
  }

  .contact {
    position: absolute;
    left: 361px;
    top: 98px;
    color: var(--gold-text);
  }
  .contact__name {
    font-size: 19px;
    font-weight: 700;
    line-height: 24px;
  }
  .contact__role {
    font-size: 15px;
    font-weight: 400;
    line-height: 20px;
  }
  .contact__rule {
    width: 24px;
    height: 2px;
    background: var(--gold-text);
    margin: 15px 0 17px;
  }
  .contact__list { list-style: none; }
  .contact__item {
    display: flex;
    align-items: center;
    gap: 6px;
    font-size: 14.5px;
    line-height: 21px;
  }
  .contact__icon {
    width: 13px;
    height: 13px;
    flex: none;
  }
</style>
</head>
<body>
<main class="canvas">
  <section class="card card--front">
    <div class="front-mark">
      <span class="front-mark__dot"></span>
      <span class="front-mark__name">Vantor Medica</span>
    </div>
  </section>

  <section class="card card--back">
    <div class="brand">
      <span class="brand__dot"></span>
      <span class="brand__name">Vantor Medica</span>
    </div>

    <div class="contact">
      <p class="contact__name">Daniel Whitford</p>
      <p class="contact__role">President</p>
      <div class="contact__rule"></div>
      <ul class="contact__list">
        <li class="contact__item">
          <svg class="contact__icon" viewBox="0 0 16 16" aria-hidden="true">
            <path d="M3.5 1.5l2.2 2.6-1.3 1.6c.9 2 2.2 3.3 4.2 4.2l1.6-1.3 2.6 2.2-1.4 2c-5-.6-9.2-4.8-9.8-9.8z" fill="none" stroke="currentColor" stroke-width="1.4" stroke-linejoin="round"/>
          </svg>
          <span>(775) BUY-KELO</span>
        </li>
        <li class="contact__item">
          <svg class="contact__icon" viewBox="0 0 16 16" aria-hidden="true">
            <rect x="1" y="3" width="14" height="10" fill="none" stroke="currentColor" stroke-width="1.4"/>
            <path d="M1 3l7 6 7-6" fill="none" stroke="currentColor" stroke-width="1.4"/>
          </svg>
          <span>info@vantormedica.example</span>
        </li>
        <li class="contact__item">
          <svg class="contact__icon" viewBox="0 0 16 16" aria-hidden="true">
            <circle cx="8" cy="8" r="6.5" fill="none" stroke="currentColor" stroke-width="1.3"/>
            <ellipse cx="8" cy="8" rx="2.8" ry="6.5" fill="none" stroke="currentColor" stroke-width="1.1"/>
            <path d="M1.5 8h13M2.6 4.8h10.8M2.6 11.2h10.8" stroke="currentColor" stroke-width="1.1"/>
          </svg>
          <span>www.vantormedica.example</span>
        </li>
      </ul>
    </div>
  </section>
</main>
</body>
</html>
```